Business Card Design

I need a card design for Melbourne based business in Australia, called M P Concrete Services. We Concrete and excavate. Concreteing is main part of business.Commercial ,Residential and industrial.We want to be known as M P C (services) as form of abbreviation.We would like to highlight the initials with contact phone. A clean straight edge design. We have no color preference and would prefer a design that can easily be used on all parts of our business including clothing,vechiles and stationary

Industry/Entity Type

Business

Contact Information for Business Card

Hugh 0491 570 156
Peter 0491 570 157
mpcsercices@quollmail.com

```html
<!DOCTYPE html>
<html lang="en">
<head>
<meta charset="utf-8">
<title>M P Concrete Services – Business Card</title>
<link rel="stylesheet" href="https://fonts.googleapis.com/css2?family=Arimo:wght@400;700&family=Abril+Fatface&display=swap">
<style>
  :root {
    --card-bg: #ffffff;
    --ink: #000000;
    --frame: #555555;
    --band: #000000;
    --band-text: #ffffff;
    --wing-dark: #2a2a2a;
    --wing-light: #d8d8d8;
  }
  html, body {
    margin: 0;
    padding: 0;
    overflow: hidden;
    background: var(--card-bg);
  }
  .card {
    position: relative;
    width: 1200px;
    height: 671px;
    box-sizing: border-box;
    border: 1px solid var(--frame);
    background: var(--card-bg);
    overflow: hidden;
    font-family: "Arimo", Arial, sans-serif;
    color: var(--ink);
  }
  .phones {
    position: absolute;
    top: 22px;
    right: 25px;
    margin: 0;
    font-size: 27px;
    font-weight: 400;
    letter-spacing: 0.2px;
  }
  .initials {
    position: absolute;
    top: 168px;
    left: 0;
    width: 1200px;
    height: 200px;
    margin: 0;
    font-family: "Arimo", Arial, sans-serif;
    font-weight: 700;
    font-size: 200px;
    line-height: 200px;
    color: var(--ink);
  }
  .initials .letter {
    position: absolute;
    top: 0;
  }
  .initials .letter-m { left: 185px; }
  .initials .letter-p { left: 490px; }
  .initials .letter-c { left: 835px; }
  .tagline {
    position: absolute;
    top: 470px;
    left: 0;
    width: 1210px;
    margin: 0;
    text-align: center;
    font-family: "Abril Fatface", Georgia, serif;
    font-size: 40px;
    letter-spacing: 1px;
  }
  .email-bar {
    position: absolute;
    left: 0;
    bottom: 0;
    width: 1200px;
    height: 82px;
  }
  .email-bar svg {
    position: absolute;
    inset: 0;
  }
  .email {
    position: absolute;
    left: 307px;
    top: 0;
    width: 586px;
    height: 82px;
    line-height: 82px;
    text-align: center;
    color: var(--band-text);
    font-size: 36px;
    font-weight: 400;
  }
</style>
</head>
<body>
  <div class="card">
    <p class="phones">Ph: 0491570156,0491570157</p>

    <h1 class="initials" aria-label="M P C">
      <span class="letter letter-m">M</span>
      <span class="letter letter-p">P</span>
      <span class="letter letter-c">C</span>
    </h1>

    <p class="tagline">M P Concrete Services</p>

    <div class="email-bar">
      <svg width="1200" height="82" viewBox="0 0 1200 82" aria-hidden="true">
        <defs>
          <linearGradient id="wing-left" x1="0" y1="0" x2="1" y2="0">
            <stop offset="0" stop-color="var(--wing-light)"/>
            <stop offset="1" stop-color="var(--wing-dark)"/>
          </linearGradient>
          <linearGradient id="wing-right" x1="1" y1="0" x2="0" y2="0">
            <stop offset="0" stop-color="var(--wing-light)"/>
            <stop offset="1" stop-color="var(--wing-dark)"/>
          </linearGradient>
        </defs>
        <polygon points="0,42 307,2 307,80" fill="url(#wing-left)"/>
        <polygon points="1200,42 893,2 893,80" fill="url(#wing-right)"/>
        <rect x="307" y="0" width="586" height="82" fill="var(--band)"/>
      </svg>
      <div class="email">mpcsercices@quollmail.com</div>
    </div>
  </div>
</body>
</html>
```